Crestline Slate & Tile Needs a Business Card

Attached you will find your logo, my photo and design guidelines for a new business card. The final design will need two separate files to create an embossed card. The cards will be printed by www.plinkprint.com (Instructions below)
Format is the Zib SQUARE card
Crestline Slate And Tile is a brick and mortar, retail stone and tile shop.
One the front:
Crestline Slate And Tile
Gerald Finchcombe
Owner
48207 Vesper Hollow Blvd
Suite R & T
Charlotte, NC 28953
Cell: 704-555-0183
Web: www.CrestlineSlateAndTile.com
(Make each word of the domain a different or alternating color)
On the back;
Something that shows beautiful colorful tile
Follow the design guide closely please. For more information see this page that describes creating the spot gloss file: https://www.plinkprint.com/us/business-cards/design-guidelines-spot-gloss
The logo is what we would like to have raised spot glossed.
Format is the Zib SQUARE card. See attahced guidlines.

```html
<!DOCTYPE html>
<html lang="en">
<head>
<meta charset="utf-8">
<title>Crestline Slate &amp; Tile — Square Business Card</title>
<link rel="stylesheet" href="https://fonts.googleapis.com/css2?family=Tinos:wght@400;700&family=Raleway:wght@400&display=swap">
<style>
  :root {
    --backdrop: #c4c5c7;
    --card: #000000;
    --gold: #d0912f;
    --rust: #b5532a;
    --slate: #4d5b68;
    --ink: #ffffff;
    --pattern-mid: #15130f;
  }
  * { margin: 0; padding: 0; box-sizing: border-box; }
  html, body { width: 1200px; height: 900px; overflow: hidden; }
  body { background: var(--backdrop); position: relative; }

  .card {
    position: absolute;
    top: 215px;
    width: 470px;
    height: 471px;
    background: var(--card);
    overflow: hidden;
  }
  .card-front { left: 107px; }
  .card-back { left: 616px; }
  .card-band {
    position: absolute; left: 0; right: 0; bottom: 0;
    height: 18px; background: var(--gold);
  }

  /* Front */
  .brand-mark {
    position: absolute; left: 43px; top: 100px;
    display: flex; align-items: center; gap: 10px;
  }
  .brand-square { width: 14px; height: 14px; background: var(--gold); transform: rotate(45deg); }
  .brand-name {
    font-family: "Tinos", serif; font-weight: 400;
    font-size: 20px; color: var(--slate); letter-spacing: 0.5px;
  }
  .portrait {
    position: absolute; left: 278px; top: 47px;
    width: 158px; height: 156px;
    border: 2px solid var(--gold);
    padding: 9px 9px 8px;
  }
  .portrait-fill {
    width: 100%; height: 100%;
    background: radial-gradient(ellipse at 50% 45%, #5b4336 0%, #2a2522 45%, #0d0d0f 100%);
  }
  .holder-name {
    position: absolute; left: 43px; top: 262px;
    font-family: "Tinos", serif; font-weight: 700;
    font-size: 25px; color: var(--ink); letter-spacing: -0.3px;
  }
  .holder-title {
    position: absolute; left: 44px; top: 290px;
    font-family: "Raleway", sans-serif; font-size: 15px; color: var(--gold);
  }
  .rule {
    position: absolute; left: 43px; top: 308px;
    width: 393px; height: 1px; background: var(--gold);
  }
  .address {
    position: absolute; left: 47px; top: 321px;
    font-family: "Raleway", sans-serif; font-size: 15px; line-height: 17.5px;
    color: var(--ink); font-style: normal;
  }
  .contact-line {
    position: absolute; left: 47px;
    display: flex; align-items: center; gap: 9px;
    font-family: "Tinos", serif; font-size: 16.5px; color: var(--ink);
  }
  .contact-phone { top: 388px; }
  .contact-web { top: 412px; }
  .contact-icon { width: 15px; height: 15px; flex: none; }
  .web-a { color: var(--gold); }
  .web-b { color: #a0783a; }
  .web-c { color: var(--rust); }

  /* Back */
  .tile-field {
    position: absolute; inset: 0 0 18px 0;
    background:
      radial-gradient(circle at 50% 40%, #201c16 0%, var(--pattern-mid) 45%, #070707 100%);
  }
  .back-lockup {
    position: absolute; left: 0; right: 0; top: 150px;
    display: flex; flex-direction: column; align-items: center; gap: 22px;
  }
  .back-square { width: 70px; height: 70px; background: var(--gold); transform: rotate(45deg); }
  .back-name {
    font-family: "Tinos", serif; font-weight: 400;
    font-size: 34px; color: var(--ink); letter-spacing: 2px;
    margin-top: 40px; text-align: center;
  }
</style>
</head>
<body>

  <section class="card card-front">
    <div class="brand-mark">
      <span class="brand-square"></span>
      <span class="brand-name">Crestline Slate &amp; Tile</span>
    </div>

    <div class="portrait">
      <div class="portrait-fill" role="img" aria-label="Portrait photo of Gerald Finchcombe, owner"></div>
    </div>

    <h1 class="holder-name">Gerald Finchcombe</h1>
    <p class="holder-title">Owner</p>
    <div class="rule"></div>

    <address class="address">
      48207 Vesper Hollow Blvd<br>
      Suite R &amp; T<br>
      Charlotte, NC 28953
    </address>

    <p class="contact-line contact-phone">
      <svg class="contact-icon" viewBox="0 0 16 16" aria-hidden="true">
        <path d="M1 5c0-2 3-3 7-3s7 1 7 3v1h-3V5H4v1H1z" fill="#d0912f"/>
        <rect x="3" y="7" width="10" height="7" rx="1" fill="#d0912f"/>
        <rect x="6" y="9" width="4" height="3" fill="#000"/>
      </svg>
      704-555-0183
    </p>
    <p class="contact-line contact-web">
      <svg class="contact-icon" viewBox="0 0 16 16" aria-hidden="true">
        <circle cx="8" cy="8" r="7" fill="#d0912f"/>
        <path d="M4 4c2 0 3 2 2 3s-2 1-2 3M10 3c0 2 2 2 3 3M9 11c1-1 3 0 3 2" stroke="#000" stroke-width="1.6" fill="none"/>
      </svg>
      <span>www.<span class="web-a">Crestline</span><span class="web-b">Slate</span><span class="web-c">And</span>Tile.com</span>
    </p>

    <div class="card-band"></div>
  </section>

  <section class="card card-back">
    <div class="tile-field" role="img" aria-label="Faint repeating geometric tile pattern on black"></div>
    <div class="back-lockup">
      <span class="back-square"></span>
      <span class="back-name">Crestline Slate &amp; Tile</span>
    </div>
    <div class="card-band"></div>
  </section>

</body>
</html>
```